We want a hot New Design for our IT company Web Site

We have a basic website with some general information and lots of mostly words and generic pictures we want to make it look and feel a lot more modern and slick. The site needs to work on mobile devices as well as desktops.

Target Market(s)

Business customers

Industry/Entity Type

It Company

Coding

Coded - Design and coding required

Number of Pages Required

5+ page

Requirements
Must have
• Sleek new Design making it look and feel more modern and less boring
Nice to have
• If it can have a better flow to it rather then have the std Drop down menus it has now.

```html
<!DOCTYPE html>
<html lang="en">
<head>
<meta charset="utf-8">
<title>Kestrel Solutions Group</title>
<link href="https://fonts.googleapis.com/css2?family=Open+Sans:wght@400;600;700&display=swap" rel="stylesheet">
<style>
:root{
  --brand:#1565c0;
  --brand-dark:#0d3f86;
  --brand-deep:#0a2f66;
  --nav-top:#3c4a5c;
  --nav-bottom:#1f2936;
  --nav-active:#8a96a4;
  --ink:#333b44;
  --muted:#7a838c;
  --rule:#c9ced4;
  --footer:#2b2f34;
  --footer-deep:#1c1f23;
  --white:#ffffff;
}
*{box-sizing:border-box;margin:0;padding:0}
html,body{width:700px;height:1200px;overflow:hidden;background:var(--white)}
body{font-family:'Open Sans',Arial,sans-serif;color:var(--ink)}
.page{position:relative;width:700px;height:1200px;overflow:hidden}

/* header */
.site-header{position:absolute;left:0;top:0;width:700px;height:70px;background:var(--white)}
.brand{position:absolute;left:72px;top:18px;display:flex;align-items:center;gap:8px}
.brand-square{width:30px;height:30px;background:var(--brand)}
.brand-name{font-size:15px;font-weight:700;color:var(--brand-deep);letter-spacing:.5px;line-height:1}
.call{position:absolute;right:72px;top:22px;display:flex;align-items:center;gap:7px}
.call-label{font-size:9px;color:var(--muted);line-height:1.2}
.call-number{font-size:15px;font-weight:700;color:var(--brand-dark);line-height:1.1}

/* nav */
.main-nav{position:absolute;left:0;top:70px;width:700px;height:22px;background:linear-gradient(var(--nav-top),var(--nav-bottom))}
.main-nav ul{list-style:none;display:flex;position:absolute;left:82px;top:0;height:22px}
.main-nav li{font-size:9px;color:var(--white);padding:0 10px;line-height:22px}
.main-nav li.active{background:var(--nav-active)}

/* hero */
.hero{position:absolute;left:0;top:92px;width:700px;height:304px;background:linear-gradient(135deg,#5f7d9c 0%,#9fb4c8 40%,#4e6580 70%,#25384f 100%)}
.hero-caption{position:absolute;left:0;bottom:0;width:700px;height:78px;background:rgba(15,25,40,.55)}
.hero-caption h1{position:absolute;left:82px;top:12px;width:420px;font-size:15px;font-weight:600;line-height:1.3;color:var(--white)}
.slider-arrow{position:absolute;top:92px;width:12px;height:16px;background:rgba(20,30,40,.8)}
.slider-arrow.prev{left:0}
.slider-arrow.next{right:0}

/* section titles */
.section-title{position:absolute;left:0;width:700px;text-align:center;font-size:15px;font-weight:600}
.section-rule{position:absolute;left:230px;width:240px;height:1px;background:var(--rule)}

/* about */
.about-text{position:absolute;left:130px;top:434px;width:440px;text-align:center;font-size:7px;line-height:1.5;color:var(--muted)}

/* services */
.services{position:absolute;left:0;top:466px;width:700px;height:326px;background:radial-gradient(ellipse at 50% 40%,#1e7ad6 0%,var(--brand) 45%,var(--brand-dark) 100%)}
.services .section-title{top:32px;color:var(--white)}
.services .section-rule{top:57px;background:rgba(255,255,255,.5)}
.services-intro{position:absolute;left:0;top:66px;width:700px;text-align:center;font-size:7px;color:#d5e4f5}
.service-center{position:absolute;left:302px;top:80px;width:96px;height:56px;border-radius:50%;background:rgba(255,255,255,.18);display:flex;align-items:center;justify-content:center;font-size:11px;font-weight:700;color:var(--white)}
.service{position:absolute;width:90px;text-align:center}
.service .ring{width:44px;height:44px;margin:0 auto;border-radius:50%;border:2px solid var(--white);display:flex;align-items:center;justify-content:center}
.service span{display:block;margin-top:5px;font-size:8px;color:var(--white)}

/* blog */
.blog .section-title{top:830px}
.blog .section-rule{top:855px}
.post{position:absolute;top:880px;width:180px}
.post-thumb{position:absolute;left:0;top:0;width:36px;height:36px;background:linear-gradient(#c7ccd2,#8d959e)}
.post-title{position:absolute;left:44px;top:0;font-size:10px;line-height:1.2;color:var(--ink)}
.post-date{position:absolute;left:44px;top:26px;font-size:7px;color:var(--muted)}
.post-excerpt{position:absolute;left:0;top:44px;width:180px;font-size:7px;line-height:1.45;color:var(--muted)}
.read-more{position:absolute;left:0;top:94px;font-size:6px;border:1px solid var(--rule);padding:2px 6px;color:var(--ink)}

/* footer */
.site-footer{position:absolute;left:0;top:984px;width:700px;height:216px;background:linear-gradient(135deg,#3a3f45,var(--footer) 50%,var(--footer-deep))}
.footer-heading{position:absolute;left:30px;top:12px;font-size:9px;color:var(--white)}
.contact-list{position:absolute;left:30px;top:32px;list-style:none}
.contact-list li{display:flex;gap:8px;margin-bottom:7px}
.contact-icon{width:14px;height:14px;flex:none;display:flex;align-items:center;justify-content:center}
.contact-label{font-size:7px;color:var(--white);line-height:1.3}
.contact-value{font-size:7px;color:#aab0b7;line-height:1.3}
.inquiry{position:absolute;left:432px;top:12px;width:236px;height:168px;background:rgba(255,255,255,.12)}
.inquiry h2{position:absolute;left:28px;top:6px;font-size:11px;font-weight:700;color:var(--white);letter-spacing:.5px}
.inquiry-icon{position:absolute;left:8px;top:7px}
.inquiry p{position:absolute;left:8px;top:26px;width:220px;font-size:6px;color:#c4c9cf}
.field{position:absolute;left:8px;width:220px;height:16px;background:rgba(0,0,0,.35);font-size:6px;color:#9aa1a9;padding:4px 6px}
.field.message{height:38px}
.submit{position:absolute;left:8px;top:143px;width:54px;height:16px;background:var(--brand);color:var(--white);font-size:7px;font-weight:700;text-align:center;line-height:16px}
.copyright{position:absolute;left:0;bottom:0;width:700px;height:12px;background:#111316;text-align:center;font-size:6px;line-height:12px;color:#8a9097}
</style>
</head>
<body>
<div class="page">

  <header class="site-header">
    <div class="brand"><div class="brand-square"></div><div class="brand-name">KESTREL<br><span style="font-size:8px;font-weight:700">SOLUTIONS GROUP</span></div></div>
    <div class="call">
      <svg width="18" height="18" viewBox="0 0 24 24"><path fill="#0d3f86" d="M6.6 10.8a15 15 0 0 0 6.6 6.6l2.2-2.2c.3-.3.7-.4 1-.2 1.1.4 2.3.6 3.6.6.6 0 1 .4 1 1V20c0 .6-.4 1-1 1A17 17 0 0 1 3 4c0-.6.4-1 1-1h3.5c.6 0 1 .4 1 1 0 1.3.2 2.5.6 3.6.1.3 0 .7-.2 1z"/></svg>
      <div><div class="call-label">Call Us Today</div><div class="call-number">07 3000 4812</div></div>
    </div>
  </header>

  <nav class="main-nav">
    <ul>
      <li class="active">Home</li><li>Consult</li><li>Procure</li><li>Provision</li><li>Cloud &amp; Connectivity</li><li>Software Development</li><li>Blog</li><li>Contact Us</li>
    </ul>
  </nav>

  <section class="hero" role="img" aria-label="Businessman holding a tablet with cloud computing and device icons floating above">
    <div class="slider-arrow prev"></div>
    <div class="slider-arrow next"></div>
    <div class="hero-caption">
      <h1>Kestrel Solutions Group Offers Technology Consultancy, Managed IT Services And A Resilient Cloud Platform For The SMB Sector</h1>
    </div>
  </section>

  <section class="about">
    <h2 class="section-title" style="top:404px">About Us</h2>
    <div class="section-rule" style="top:428px"></div>
    <p class="about-text">Kestrel Solutions Group offers technology consultancy, managed IT services and a resilient cloud platform for the SMB sector. With offices in Brisbane and Melbourne, we specialise in meeting the mission critical needs of your business.</p>
  </section>

  <section class="services">
    <h2 class="section-title">Services We Offer</h2>
    <div class="section-rule"></div>
    <p class="services-intro">Some information is the gold to your business. We can recover data from corrupted disks.</p>
    <div class="service-center">KESTREL</div>

    <div class="service" style="left:60px;top:86px"><div class="ring"><svg width="22" height="22" viewBox="0 0 24 24" fill="#fff"><circle cx="8" cy="8" r="3"/><circle cx="16" cy="8" r="3"/><path d="M2 19c0-3 3-5 6-5s6 2 6 5zM11 19c0-3 2-5 5-5s6 2 6 5z"/></svg></div><span>Consult</span></div>
    <div class="service" style="left:118px;top:172px"><div class="ring"><svg width="22" height="22" viewBox="0 0 24 24" fill="#fff"><path d="M3 4h3l2 10h10l2-7H7" stroke="#fff" stroke-width="2" fill="none"/><circle cx="9" cy="19" r="2"/><circle cx="17" cy="19" r="2"/></svg></div><span>Procure</span></div>
    <div class="service" style="left:223px;top:197px"><div class="ring"><svg width="22" height="22" viewBox="0 0 24 24"><circle cx="12" cy="12" r="7" fill="none" stroke="#fff" stroke-width="4" stroke-dasharray="3 2.5"/><circle cx="12" cy="12" r="3" fill="#fff"/></svg></div><span>Provision</span></div>
    <div class="service" style="left:335px;top:212px"><div class="ring"><svg width="24" height="18" viewBox="0 0 24 18" fill="#fff"><path d="M6 16a5 5 0 0 1 0-10 6 6 0 0 1 11-1 5 5 0 0 1 1 11z"/></svg></div><span>Cloud &amp; Connectivity</span></div>
    <div class="service" style="left:455px;top:174px"><div class="ring"><svg width="22" height="22" viewBox="0 0 24 24" fill="#fff"><rect x="3" y="4" width="18" height="12" rx="1"/><rect x="9" y="17" width="6" height="3"/></svg></div><span>Manage</span></div>
    <div class="service" style="left:533px;top:86px"><div class="ring"><svg width="22" height="22" viewBox="0 0 24 24" fill="none" stroke="#fff" stroke-width="2"><path d="M8 6l-6 6 6 6M16 6l6 6-6 6"/></svg></div><span>Software Development</span></div>
  </section>

  <section class="blog">
    <h2 class="section-title">Blog Posts</h2>
    <div class="section-rule"></div>

    <article class="post" style="left:74px">
      <div class="post-thumb" role="img" aria-label="Author portrait"></div>
      <h3 class="post-title">Consecutive<br>Partnership</h3>
      <div class="post-date">20th Jan, 2015</div>
      <p class="post-excerpt">Lorem ipsum dolor sit amet, consectetuer adipiscing elit, sed diam nonummy nibh euismod tincidunt ut laoreet dolore magna aliquam erat volutpat.</p>
      <div class="read-more">READ MORE</div>
    </article>
    <article class="post" style="left:290px">
      <div class="post-thumb" role="img" aria-label="Author portrait"></div>
      <h3 class="post-title">Cloud Data<br>Transfer</h3>
      <div class="post-date">22nd Jan, 2015</div>
      <p class="post-excerpt">Lorem ipsum dolor sit amet, consectetuer adipiscing elit, sed diam nonummy nibh euismod tincidunt ut laoreet dolore magna aliquam erat volutpat.</p>
      <div class="read-more">READ MORE</div>
    </article>
    <article class="post" style="left:480px">
      <div class="post-thumb" role="img" aria-label="Author portrait"></div>
      <h3 class="post-title">Moving Data into<br>the Cloud</h3>
      <div class="post-date">28th Feb, 2015</div>
      <p class="post-excerpt">Lorem ipsum dolor sit amet, consectetuer adipiscing elit, sed diam nonummy nibh euismod tincidunt ut laoreet dolore magna aliquam erat volutpat.</p>
      <div class="read-more">READ MORE</div>
    </article>
  </section>

  <footer class="site-footer">
    <h2 class="footer-heading">Contact Information</h2>
    <ul class="contact-list">
      <li><span class="contact-icon"><svg width="10" height="13" viewBox="0 0 10 13"><path fill="#fff" d="M5 0a5 5 0 0 0-5 5c0 4 5 8 5 8s5-4 5-8a5 5 0 0 0-5-5zm0 7a2 2 0 1 1 0-4 2 2 0 0 1 0 4z"/></svg></span><div><div class="contact-label">Main Office</div><div class="contact-value">Level 2, 18 Harbour Lane, Northgate, Brisbane, Queensland 4000</div></div></li>
      <li><span class="contact-icon"><svg width="12" height="12" viewBox="0 0 24 24"><path fill="#fff" d="M6.6 10.8a15 15 0 0 0 6.6 6.6l2.2-2.2c.3-.3.7-.4 1-.2 1.1.4 2.3.6 3.6.6.6 0 1 .4 1 1V20c0 .6-.4 1-1 1A17 17 0 0 1 3 4c0-.6.4-1 1-1h3.5c.6 0 1 .4 1 1 0 1.3.2 2.5.6 3.6.1.3 0 .7-.2 1z"/></svg></span><div><div class="contact-label">Telephone</div><div class="contact-value">1300 300 819</div></div></li>
      <li><span class="contact-icon"><svg width="12" height="9" viewBox="0 0 12 9"><rect width="12" height="9" fill="#fff"/><path d="M0 0l6 5 6-5" stroke="#2b2f34" fill="none"/></svg></span><div><div class="contact-label">Email</div><div class="contact-value">info@kestrelsg.com.au</div></div></li>
      <li><span class="contact-icon"><svg width="12" height="12"><circle cx="6" cy="6" r="6" fill="#5a6168"/></svg></span><div><div class="contact-label">Facebook</div><div class="contact-value">facebook.com/kestrelsolutions</div></div></li>
      <li><span class="contact-icon"><svg width="12" height="12"><circle cx="6" cy="6" r="6" fill="#5a6168"/></svg></span><div><div class="contact-label">Twitter</div><div class="contact-value">twitter.com/kestrelsg</div></div></li>
    </ul>

    <form class="inquiry">
      <svg class="inquiry-icon" width="14" height="12" viewBox="0 0 14 12"><path fill="#fff" d="M1 1h12v8H5l-3 3V9H1z"/></svg>
      <h2>QUICK INQUIRY</h2>
      <p>Fill out the form below and we will be in touch within 24 hours.</p>
      <div class="field" style="top:44px">Name</div>
      <div class="field" style="top:66px">Email</div>
      <div class="field message" style="top:88px">Message</div>
      <div class="submit">SUBMIT</div>
    </form>

    <div class="copyright">Copyright © 2015 Kestrel Solutions Group. All Rights Reserved.</div>
  </footer>

</div>
</body>
</html>
```